Marrowfield Transport Company Business Card Design

We are a company that delivers natural saltwater (from the ocean) to aquarium companies, restaurants and home marine tanks. I would like a new business card to suit.

Must include Name, company name, abn, contact number and website as well as logo (see attached).

Looking for a design that stands out, has a clean but unique appearance.

Double and single sided entries welcome

• Logo

```html
<!DOCTYPE html>
<html lang="en">
<head>
<meta charset="utf-8">
<title>Marrowfield Transport Company – Business Card</title>
<link rel="stylesheet" href="https://fonts.googleapis.com/css2?family=Open+Sans:wght@400;600;700&display=swap">
<style>
  :root {
    --ocean: #1f9ad8;
    --ocean-deep: #168bc9;
    --ocean-light: #5fcaf4;
    --ink-blue: #1a8fd0;
    --paper: #ffffff;
    --backdrop: #e9ecef;
    --shadow: rgba(0, 0, 0, 0.18);
  }
  * { margin: 0; padding: 0; box-sizing: border-box; }
  html, body {
    width: 1200px;
    height: 871px;
    overflow: hidden;
  }
  body {
    background: var(--backdrop);
    font-family: "Open Sans", Arial, sans-serif;
    display: flex;
    align-items: center;
    justify-content: center;
    gap: 40px;
  }
  .card {
    position: relative;
    width: 540px;
    height: 327px;
    overflow: hidden;
    box-shadow: 0 10px 30px var(--shadow);
  }

  /* Back side: blue with contact details */
  .card--back {
    background: linear-gradient(135deg, var(--ocean-deep), var(--ocean) 60%, #2aa8e2);
    color: var(--paper);
  }
  .back-wave-area {
    position: absolute;
    right: 0;
    bottom: 0;
    width: 240px;
    height: 110px;
    background: linear-gradient(180deg, rgba(95, 202, 244, 0.55), var(--ocean-light));
  }
  .back-brand {
    position: absolute;
    left: 34px;
    top: 138px;
    display: flex;
    align-items: center;
    gap: 12px;
  }
  .back-brand-dot {
    width: 22px;
    height: 22px;
    border-radius: 50%;
    background: var(--paper);
    flex: none;
  }
  .back-brand-name {
    font-weight: 700;
    font-size: 19px;
    line-height: 1.15;
    color: var(--paper);
  }
  .contact {
    position: absolute;
    left: 258px;
    top: 44px;
    width: 260px;
  }
  .contact-name {
    font-size: 19px;
    font-weight: 400;
    padding-bottom: 5px;
    border-bottom: 2px solid var(--paper);
  }
  .contact-role {
    font-size: 11px;
    margin-left: 4px;
  }
  .contact-list {
    list-style: none;
    margin-top: 8px;
    font-size: 11.5px;
    line-height: 1.55;
  }
  .contact-label {
    display: inline-block;
    width: 14px;
  }

  /* Front side: white with company name */
  .card--front {
    background: var(--paper);
  }
  .front-name {
    position: absolute;
    left: 0;
    right: 0;
    top: 70px;
    text-align: center;
    color: var(--ink-blue);
    font-weight: 600;
    line-height: 1.05;
  }
  .front-name-main {
    display: block;
    font-size: 62px;
    letter-spacing: -1px;
  }
  .front-name-sub {
    display: block;
    font-size: 30px;
  }
  .front-wave-area {
    position: absolute;
    left: 0;
    right: 0;
    bottom: 0;
    height: 66px;
    background: linear-gradient(180deg, #3aaee4, var(--ocean));
  }
</style>
</head>
<body>

  <section class="card card--back" aria-label="Card back">
    <div class="back-wave-area" role="img" aria-label="Decorative ocean wave"></div>
    <div class="back-brand">
      <span class="back-brand-dot"></span>
      <span class="back-brand-name">Marrowfield<br>Transport Company</span>
    </div>
    <div class="contact">
      <p class="contact-name">Dana Holt<span class="contact-role">Manager</span></p>
      <ul class="contact-list">
        <li><span class="contact-label">E</span>info@marrowfieldtransport.com.au</li>
        <li><span class="contact-label">P</span>+61 400 118 274</li>
        <li><span class="contact-label">W</span>www.marrowfieldtransport.com.au</li>
      </ul>
    </div>
  </section>

  <section class="card card--front" aria-label="Card front">
    <p class="front-name">
      <span class="front-name-main">Marrowfield</span>
      <span class="front-name-sub">Transport Company</span>
    </p>
    <div class="front-wave-area" role="img" aria-label="Decorative ocean wave band"></div>
  </section>

</body>
</html>
```